Business Card New Design for Veltrix

We would like a new look on our business card, using the same style, the same colors blue, gray and white with similar font that is represented on the new Sell Sheet. We recently re-designed our Sell Sheets - I've attached a sell sheet file for your reference. I've also attached our current business card and our logo. Keep the same information listed on each side of the card.

Contact Information for Business Card

Use details given on example provided

Font styles to use
Other font styles liked:
• Myriad Regular and Bold

Colors

Designer to choose colors to be used in the design.

Requirements
Must have
• Current Information that was provided on the current business card. Colors Must use Blue, Gray and White, the same colors as the sell sheet example.

```html
<!DOCTYPE html>
<html lang="en">
<head>
<meta charset="utf-8">
<title>Veltrix Business Card</title>
<link href="https://fonts.googleapis.com/css2?family=Source+Sans+3:wght@400;600;700&display=swap" rel="stylesheet">
<style>
  :root {
    --blue: #0a14f0;
    --gray: #4d4d4f;
    --ink: #2e2e30;
    --white: #ffffff;
    --backdrop: #d6d6d8;
  }
  * { margin: 0; padding: 0; box-sizing: border-box; }
  html, body {
    width: 1200px; height: 801px; overflow: hidden;
    background: var(--backdrop);
    font-family: "Source Sans 3", Arial, sans-serif;
  }
  .card {
    position: absolute; width: 560px; height: 320px;
    background: var(--white); overflow: hidden;
    box-shadow: 0 6px 18px rgba(0,0,0,0.18);
  }
  .card--front { left: 60px; top: 50px; }
  .card--back { left: 580px; top: 430px; }
  .card__shapes { position: absolute; inset: 0; }

  .nameplate {
    position: absolute; left: 22px; top: 22px;
    color: var(--white); font-size: 21px; letter-spacing: 0.5px;
    display: flex; align-items: center; gap: 12px; white-space: nowrap;
  }
  .nameplate__first { font-weight: 700; }
  .nameplate__last { font-weight: 400; }
  .nameplate__bar { width: 2px; height: 24px; background: var(--white); }
  .nameplate__role { font-size: 16px; font-weight: 400; }

  .brand {
    position: absolute; left: 40px; width: 250px;
    display: flex; flex-direction: column; align-items: center;
  }
  .card--front .brand { top: 148px; }
  .card--back .brand { top: 120px; }
  .brand__name {
    display: flex; align-items: center; gap: 10px;
    font-size: 46px; font-weight: 600; letter-spacing: 5px;
    color: var(--gray); text-transform: uppercase; line-height: 1;
  }
  .brand__dot { width: 12px; height: 12px; border-radius: 50%; background: var(--blue); }
  .brand__tagline {
    margin-top: 10px; text-align: center;
    font-size: 20px; line-height: 1.15; color: var(--ink);
  }

  .divider {
    position: absolute; width: 2px; background: var(--blue);
  }
  .card--front .divider { left: 305px; top: 118px; height: 150px; }
  .card--back .divider { left: 300px; top: 90px; height: 170px; }

  .contact {
    position: absolute; left: 325px; top: 112px;
    font-size: 12.5px; line-height: 1.45; color: var(--ink);
  }
  .contact__address { margin-bottom: 6px; }
  .contact__row { display: flex; align-items: center; gap: 8px; }
  .contact__icon { width: 11px; height: 11px; flex: none; }
  .contact__accent { color: var(--blue); }

  .catalog { position: absolute; left: 322px; top: 82px; color: var(--ink); }
  .catalog__title { font-size: 24px; font-weight: 600; line-height: 1.1; }
  .catalog__rule { width: 34px; height: 2px; background: var(--blue); margin: 4px 0 6px; }
  .catalog__list { list-style: none; font-size: 13.5px; font-weight: 600; line-height: 1.42; }
</style>
</head>
<body>

<section class="card card--front">
  <svg class="card__shapes" viewBox="0 0 560 320" width="560" height="320" aria-hidden="true">
    <path fill="var(--gray)" d="M470 0 L560 0 L560 72 Z"/>
    <path fill="var(--blue)" d="M0 16 L250 16 C330 16 380 0 450 0 C495 0 530 30 560 72 L560 82 C525 45 490 26 445 28 C385 30 340 52 275 52 L0 52 Z"/>
  </svg>
  <div class="nameplate">
    <span><span class="nameplate__first">MARCUS</span> <span class="nameplate__last">HALE</span></span>
    <span class="nameplate__bar"></span>
    <span class="nameplate__role">CEO</span>
  </div>

  <div class="brand">
    <div class="brand__name"><span class="brand__dot"></span>Veltrix</div>
    <div class="brand__tagline">Veltrix Technical<br>Services, Inc.</div>
  </div>

  <div class="divider"></div>

  <div class="contact">
    <div class="contact__address">4170 Larkspur Avenue,<br>Elmwood, IL 60499</div>
    <div class="contact__row">
      <svg class="contact__icon" viewBox="0 0 12 12"><path fill="var(--ink)" d="M1 4 C1 2 3 1 6 1 C9 1 11 2 11 4 L8.5 5 L8 3.8 C7 3.5 5 3.5 4 3.8 L3.5 5 Z M2.5 7 L9.5 7 L10 11 L2 11 Z"/></svg>
      <span>(888) 555-0142x318 (toll free)</span>
    </div>
    <div class="contact__row">
      <svg class="contact__icon" viewBox="0 0 12 12"><path fill="var(--ink)" d="M1 4 C1 2 3 1 6 1 C9 1 11 2 11 4 L8.5 5 L8 3.8 C7 3.5 5 3.5 4 3.8 L3.5 5 Z M2.5 7 L9.5 7 L10 11 L2 11 Z"/></svg>
      <span>(815) 555-0142</span>
    </div>
    <div class="contact__row">
      <svg class="contact__icon" viewBox="0 0 12 12"><path fill="none" stroke="var(--ink)" stroke-width="1.4" d="M2 1.5 L4 1.5 L5 4 L3.8 5 C4.5 6.8 5.5 7.8 7 8.5 L8 7.2 L10.5 8.2 L10.5 10.3 C6 10.5 1.5 6 2 1.5 Z"/></svg>
      <span>(815) 555-0177</span>
    </div>
    <div class="contact__row">
      <svg class="contact__icon" viewBox="0 0 12 12"><rect x="3" y="0.8" width="6" height="10.4" rx="1" fill="none" stroke="var(--ink)" stroke-width="1.2"/><circle cx="6" cy="9.4" r="0.7" fill="var(--ink)"/></svg>
      <span>(815) 555-0190</span>
    </div>
    <div class="contact__row">
      <svg class="contact__icon" viewBox="0 0 12 12"><rect x="0.8" y="2.5" width="10.4" height="7" fill="var(--ink)"/><path d="M0.8 2.5 L6 6.5 L11.2 2.5" fill="none" stroke="var(--white)" stroke-width="1"/></svg>
      <span>mhale@<span class="contact__accent">v-t-s</span>.com</span>
    </div>
    <div class="contact__row">
      <svg class="contact__icon" viewBox="0 0 12 12"><circle cx="6" cy="6" r="5" fill="none" stroke="var(--ink)" stroke-width="1.1"/><ellipse cx="6" cy="6" rx="2.2" ry="5" fill="none" stroke="var(--ink)" stroke-width="0.9"/><path d="M1 6 H11 M2 3.5 H10 M2 8.5 H10" stroke="var(--ink)" stroke-width="0.9"/></svg>
      <span>www.<span class="contact__accent">v-t-s</span>.com</span>
    </div>
  </div>
</section>

<section class="card card--back">
  <svg class="card__shapes" viewBox="0 0 560 320" width="560" height="320" aria-hidden="true">
    <rect x="330" y="0" width="230" height="320" fill="var(--blue)"/>
    <path fill="var(--white)" d="M0 0 L390 0 C450 0 500 30 525 75 C550 120 552 190 535 235 C520 275 495 300 465 320 L0 320 Z"/>
  </svg>

  <div class="brand">
    <div class="brand__name"><span class="brand__dot"></span>Veltrix</div>
    <div class="brand__tagline">Veltrix Technical<br>Services, Inc.</div>
  </div>

  <div class="divider"></div>

  <div class="catalog">
    <h2 class="catalog__title">Conveyors</h2>
    <div class="catalog__rule"></div>
    <ul class="catalog__list">
      <li>Target Sauce Applicators</li>
      <li>Target Topping Applicators</li>
      <li>Waterfall Topping Applicators</li>
      <li>Pepperoni/Meat Slicer/Applicators</li>
      <li>Portion Controlled Filler Pumps</li>
      <li>Dry Ingredient Applicators</li>
      <li>Check Weigh Conveyors</li>
      <li>Portion Compensators</li>
    </ul>
  </div>
</section>

</body>
</html>
```